inspirational business card

I want to use the Vector on Pixavend.com (number 58172046) and I will purchase the vector to send it to the designer once the general concept is approved. You can download it for free for a one time use on providing a design for this request.
Within the vector, insert:
Tessa Brundle
Guidance and Partnering

I prefer a vertical card but do not require vertical.

Contact info:

Tessa Brundle, J.D.
Collaborative Lawyer
Certified Divorce Coach
Mediation Coach
PHONE 515/555-0143
EMAIL: tbjd@quellmail.net

Website: Guidanceandpartnering.com
Settlementcourse.com

I like greens, blue and grey. I do not want black font, and would like the font to be legible without needing perfect reading vision (no super small font).
I would like the overall theme to convey growth and nurturance.
I like the vector I selected because of the growth and light portrayed.
Not too frilly or too bold. I would like to to appeal to both sexes.

Target Market(s)

Generally professional women 35-60

Industry/Entity Type

Attorney

Font styles to use
Serif
Sans Serif

Colors
acd136
cadf82
fbf289
9d9d9d

Requirements
Must have
• My project does not need to have my photo but you could use it if you want
Nice to have
• Vertical
• I like rounded edges on the cards
Should not have
• I do not like my name appearing two times in close proximity. I'm not a flowery person.

```html
<!DOCTYPE html>
<html lang="en">
<head>
<meta charset="utf-8">
<title>Tessa Brundle – Business Card</title>
<link href="https://fonts.googleapis.com/css2?family=Libre+Baskerville&family=Open+Sans:wght@400;600&display=swap" rel="stylesheet">
<style>
  :root{
    --stage:#1c1c1c;
    --card-front:#ffffff;
    --card-back:#9d9d9d;
    --green:#acd136;
    --green-soft:#cadf82;
    --grey-text:#8a8a8a;
    --white:#ffffff;
  }
  *{margin:0;padding:0;box-sizing:border-box}
  html,body{width:1200px;height:963px;overflow:hidden;background:var(--stage)}
  .stage{position:relative;width:1200px;height:963px}
  .card{position:absolute;top:333px;width:520px;height:297px;border-radius:18px;overflow:hidden}
  .card--front{left:50px;background:var(--card-front)}
  .card--back{left:630px;background:var(--card-back)}

  .serif{font-family:"Libre Baskerville",Georgia,serif}
  .sans{font-family:"Open Sans",Arial,sans-serif}

  /* front: practice block */
  .practice{position:absolute;left:50px;top:24px;width:250px;text-align:center}
  .practice__mark{display:block;margin:0 auto 12px;width:78px;height:78px;border-radius:50%;background:var(--green)}
  .practice__name{font-size:15px;letter-spacing:1px;color:var(--grey-text);line-height:1;text-transform:uppercase}

  /* front: contacts */
  .contacts{position:absolute;left:28px;top:150px;list-style:none}
  .contacts li{display:flex;align-items:center;gap:8px;font-size:12px;color:var(--grey-text);line-height:21px}
  .contacts svg{width:10px;height:10px;fill:var(--green);flex:none}

  /* front: signature block */
  .person{position:absolute;right:26px;top:176px;text-align:right}
  .person__name{font-size:14px;letter-spacing:1px;color:var(--green);text-transform:uppercase;margin-bottom:3px}
  .person__role{font-size:11px;color:var(--grey-text);line-height:16px}

  .band{position:absolute;left:190px;right:0;bottom:0;height:6px;background:var(--green)}
  .tab{position:absolute;right:0;top:176px;width:6px;height:36px;background:var(--green)}

  /* back */
  .back-brand{position:absolute;left:0;right:0;top:60px;text-align:center;color:var(--white)}
  .back-brand__mark{display:block;margin:0 auto 16px;width:96px;height:96px;border-radius:50%;border:6px solid var(--white)}
  .back-brand__name{font-size:26px;letter-spacing:1.5px;line-height:1;text-transform:uppercase}
  .back-brand__tag{margin-top:8px;font-size:9px;letter-spacing:1.5px;text-transform:uppercase}
</style>
</head>
<body>
<main class="stage">

  <section class="card card--front" aria-label="Card front">
    <div class="practice">
      <span class="practice__mark"></span>
      <p class="practice__name serif">Guidance and Partnering</p>
    </div>

    <ul class="contacts sans">
      <li><svg viewBox="0 0 10 10"><path d="M2 0l2 2.5-1 1.2a6 6 0 0 0 3.3 3.3l1.2-1L10 8 8.5 10C4 10 0 6 0 1.5z"/></svg>515/555-0143</li>
      <li><svg viewBox="0 0 10 10"><path d="M0 2h10v6H0zM0 2l5 3.5L10 2" stroke="#fff" stroke-width=".8"/></svg>tbjd@quellmail.net</li>
      <li><svg viewBox="0 0 10 10"><path d="M5 0L10 4.5H8.5V10h-2.5V7h-2v3H1.5V4.5H0z"/></svg>Guidanceandpartnering.com</li>
      <li><svg viewBox="0 0 10 10"><path d="M5 0L10 4.5H8.5V10h-2.5V7h-2v3H1.5V4.5H0z"/></svg>Settlementcourse.com</li>
    </ul>

    <div class="person">
      <p class="person__name serif">Tessa Brundle, J.D.</p>
      <p class="person__role sans">Collaborative Lawyer</p>
      <p class="person__role sans">Certified Divorce Coach</p>
      <p class="person__role sans">Mediation Coach</p>
    </div>

    <span class="tab"></span>
    <span class="band"></span>
  </section>

  <section class="card card--back" aria-label="Card back">
    <div class="back-brand">
      <span class="back-brand__mark"></span>
      <p class="back-brand__name serif">Tessa Brundle</p>
      <p class="back-brand__tag serif">Guidance and Partnering</p>
    </div>
  </section>

</main>
</body>
</html>
```